Can you create a clean, elegant and professional-looking World news portal design with coding?

We are looking for an initial design/concept with coding of daily world news portal . The design should be clean, elegant and professional-looking. We don't want anything too bleeding edge, and we would like to steer away from anything that looks too much like a blog. Please feel free to be creative. We are open to different styles, colour schemes etc. but it is important the design works with itself as a whole and has a consistent look and feel.

There should be at least one sidebar. We have found that most online newspapers are base white, blue, red, with a dash of colour, and I would like to suggest this as a starting point.

Top Navigation

I need a good looking Navigation bar with the following Categories U.S, World, Politics ,Business, Tech, Sport etc.

Key Sections in home Page

- Under that there should be a section for Top stories on the left side and a widget showing latest news on the right side

- Under that a section for Breaking news

- Under that a section for local news

- Below that I need the video section showing Top videos on the left side and list of videos on the right side

- Below that I need a sports section

- Below that US news section

- Below that World News

- Below that I need the Politics section

- Below that The business section

- Below that the science section

- Below that news around the web

- Below that the entertainment section

All these sections should have a top story on the left and list of stories on the right.

I need a logo designer for news portal

```html
<!DOCTYPE html>
<html lang="en">
<head>
<meta charset="utf-8">
<title>Daily World News Portal</title>
<link rel="stylesheet" href="https://fonts.googleapis.com/css2?family=Oswald:wght@400;500&family=Open+Sans:wght@400;600;700&display=swap">
<style>
:root{
  --red:#e3262f;
  --dark:#1f1f21;
  --ink:#222;
  --text:#444;
  --muted:#8a8a8a;
  --line:#dedede;
  --soft:#f3f3f3;
  --footer:#1b1b1c;
  --footer-bottom:#111112;
  --link:#1f5f9e;
}
*{box-sizing:border-box;margin:0;padding:0}
html,body{width:1200px;height:4905px;overflow:hidden;background:#fff}
body{font-family:"Open Sans",Arial,sans-serif;color:var(--text);font-size:12px;line-height:1.45}
a{color:inherit;text-decoration:none}
ul{list-style:none}
.wrap{width:1108px;margin:0 auto}

/* utility bar */
.utility{height:33px;background:var(--dark);color:#ddd;font-size:10px;font-weight:600;letter-spacing:.3px}
.utility .wrap{display:flex;justify-content:space-between;align-items:center;height:33px}
.utility nav{display:flex;gap:18px;align-items:center}
.utility span{display:flex;align-items:center;gap:6px}
.utility svg{width:11px;height:11px}

/* masthead */
.masthead{height:107px}
.masthead .wrap{display:flex;align-items:center;height:107px}
.brand{font-family:"Oswald",sans-serif;font-weight:500;font-size:40px;color:var(--ink);letter-spacing:.5px;width:430px}
.search{display:flex;height:34px;border:1px solid var(--line)}
.search .field{width:250px;padding:0 10px;font-size:11px;color:var(--muted);display:flex;align-items:center}
.search .scope{width:132px;border-left:1px solid var(--line);padding:0 10px;font-size:11px;color:var(--ink);display:flex;align-items:center;justify-content:space-between}
.search .go{width:36px;background:var(--dark);display:flex;align-items:center;justify-content:center}
.weather{margin-left:auto;font-size:11px;font-weight:600;color:var(--ink);display:flex;align-items:center;gap:8px}

/* main navigation */
.primary-nav{height:40px;background:var(--red)}
.primary-nav ul{display:flex;height:40px;align-items:center}
.primary-nav li{color:#fff;font-size:12px;font-weight:600;padding:0 16px;text-transform:uppercase;height:40px;display:flex;align-items:center}
.primary-nav li.active{background:#b81c24}

/* ticker */
.ticker{margin-top:6px;height:34px;display:flex;align-items:center;border:1px solid var(--line)}
.ticker .label{background:var(--dark);color:#fff;font-weight:700;font-size:12px;height:100%;display:flex;align-items:center;padding:0 14px;text-transform:uppercase}
.ticker .line{flex:1;padding:0 14px;font-size:12px;color:var(--ink)}
.ticker .line b{color:var(--red);margin-right:6px}

/* rows */
.row{display:grid;grid-template-columns:794px 280px;column-gap:34px;overflow:hidden}
.r1{margin-top:10px;height:420px}
.r2{height:380px;padding-top:22px}
.r3{height:600px;padding-top:22px}
.r4{height:370px;padding-top:30px}
.r5{height:360px;padding-top:30px}
.r6{height:350px;padding-top:20px}
.r7{height:410px;padding-top:24px}
.r8{height:350px;padding-top:24px}
.r9{height:330px;padding-top:20px}
.r10{height:350px;padding-top:20px}
.r11{height:428px;padding-top:24px}

/* section heads */
.sec-head{display:flex;align-items:center;justify-content:space-between;border-bottom:2px solid var(--red);padding-bottom:4px;margin-bottom:18px;height:36px}
.sec-head h2,.side-title{font-family:"Oswald",sans-serif;font-weight:400;font-size:24px;color:var(--red);text-transform:uppercase;letter-spacing:.3px;line-height:1}
.side-title{border-bottom:2px solid var(--red);padding-bottom:6px;margin-bottom:12px;height:36px;display:flex;align-items:flex-end}
.pager{display:flex;gap:3px}
.pager i{width:20px;height:20px;background:#555;display:flex;align-items:center;justify-content:center}
.pager i:last-child{background:var(--dark)}
.pager svg{width:8px;height:8px}

/* hero slider */
.hero{position:relative;height:410px;background:linear-gradient(180deg,#c9d6e3 0%,#b9c4cc 35%,#c7a66a 62%,#8d7a5a 100%)}
.hero .shot{position:absolute;inset:0}
.hero .arrow{position:absolute;top:160px;width:22px;height:34px;background:rgba(0,0,0,.55);display:flex;align-items:center;justify-content:center}
.hero .arrow.prev{left:0}.hero .arrow.next{right:0}
.hero .caption{position:absolute;left:0;right:0;bottom:0;height:78px;background:rgba(0,0,0,.78);color:#fff;padding:14px 18px}
.hero .caption h1{font-size:20px;font-weight:700;line-height:1.2}
.hero .caption p{font-size:12px;margin-top:6px;color:#ddd}
.btn-red{position:absolute;right:16px;top:22px;background:var(--red);color:#fff;font-weight:600;font-size:13px;padding:8px 18px}

/* bullet lists */
.bullets li{position:relative;padding:6px 0 6px 14px;border-bottom:1px solid #ececec;font-size:12px;color:var(--ink);line-height:1.35}
.bullets li::before{content:"";position:absolute;left:0;top:12px;width:5px;height:5px;background:var(--red)}
.more-right{display:block;text-align:right;font-weight:700;font-size:11px;color:var(--ink);margin-top:10px;text-transform:uppercase}

/* breaking + feature */
.breaking{display:flex;align-items:center;height:36px;border:1px solid var(--line);margin-bottom:18px}
.breaking .label{background:var(--dark);color:#fff;font-weight:700;font-size:12px;height:100%;padding:0 14px;display:flex;align-items:center}
.breaking .line{padding:0 14px;font-size:12px;color:var(--ink)}
.feature{display:grid;grid-template-columns:386px 1fr;gap:22px}
.feature .photo{height:264px;background:linear-gradient(160deg,#6e7a6f 0%,#3d4640 45%,#a89c84 100%)}
.feature h3{font-size:16px;font-weight:700;color:var(--ink);line-height:1.35;margin-bottom:10px}
.feature p{font-size:12px;margin-bottom:8px}
.read{font-weight:700;font-size:11px;color:var(--ink);text-transform:uppercase}

/* two-column stories */
.story-grid{display:grid;grid-template-columns:1fr 1fr;column-gap:30px;row-gap:26px}
.story h3{font-size:13.5px;font-weight:700;color:var(--ink);line-height:1.35;display:inline}
.story .meta{font-size:10px;color:var(--muted);margin-left:6px}
.story .body{margin-top:8px;font-size:12px}
.story .thumb{float:left;width:112px;height:90px;margin:0 12px 6px 0;background:linear-gradient(135deg,#2c3e66,#7d8aa6 55%,#c0a77a)}

/* tabs */
.tabs{display:flex;gap:4px;margin-bottom:12px}
.tabs span{flex:1;text-align:center;font-size:11px;font-weight:700;text-transform:uppercase;background:var(--soft);color:var(--ink);padding:8px 0}
.tabs span.on{background:var(--dark);color:#fff}
.tabs.inline{width:220px;margin:-6px 0 16px}

/* videos */
.video-grid{display:grid;grid-template-columns:repeat(3,1fr);gap:16px}
.video .frame{position:relative;height:204px;background:linear-gradient(160deg,#3a3f4a,#7b6f62 60%,#2a2a2e)}
.video .frame svg{position:absolute;left:50%;top:50%;width:48px;height:48px;margin:-24px 0 0 -24px}
.video h3{font-size:14px;font-weight:700;color:var(--ink);margin-top:10px;text-align:center}
.vlist li{display:flex;gap:10px;padding:8px 0;border-bottom:1px solid #ececec}
.vlist .vthumb{position:relative;width:96px;height:66px;flex:none;background:linear-gradient(150deg,#4a4f5a,#9b8c78)}
.vlist .vthumb svg{position:absolute;left:36px;top:21px;width:24px;height:24px}
.vlist b{display:block;color:var(--link);font-size:13px}
.vlist p{font-size:11px;line-height:1.35}

/* card grid */
.card-grid{display:grid;grid-template-columns:repeat(4,1fr);gap:16px}
.card .pic{height:118px;background:linear-gradient(140deg,#51607a,#9aa3b0 50%,#c3a88a)}
.card h3{font-size:13.5px;font-weight:700;color:var(--ink);line-height:1.3;margin-top:10px}
.card .meta{font-size:10px;color:var(--muted);margin:3px 0 6px}
.card p{font-size:11.5px;line-height:1.45}
.card .read{display:inline-block;margin-top:3px}

/* footer */
.site-footer{margin-top:38px;height:282px;background:var(--footer);color:#bbb}
.site-footer .wrap{display:grid;grid-template-columns:repeat(5,1fr);gap:24px;padding-top:34px}
.site-footer h4{font-family:"Oswald",sans-serif;font-weight:500;font-size:15px;color:#fff;text-transform:uppercase;margin-bottom:12px;letter-spacing:.4px}
.site-footer li{font-size:10px;text-transform:uppercase;line-height:2;letter-spacing:.2px}
.legal{height:45px;background:var(--footer-bottom);color:#999;font-size:10px}
.legal .wrap{display:flex;justify-content:space-between;align-items:center;height:45px}
.legal nav{display:flex;gap:14px}
</style>
</head>
<body>

<header>
  <div class="utility">
    <div class="wrap">
      <nav>
        <span><svg viewBox="0 0 12 12"><rect x="1" y="2" width="10" height="9" fill="none" stroke="#ddd" stroke-width="1.4"/><line x1="1" y1="5" x2="11" y2="5" stroke="#ddd"/></svg>EVENTS</span>
        <span><svg viewBox="0 0 12 12"><circle cx="6" cy="6" r="4.5" fill="none" stroke="#ddd" stroke-width="1.4"/></svg>POLICE AND FIRE</span>
      </nav>
      <nav>
        <span><svg viewBox="0 0 12 12"><circle cx="6" cy="4" r="2.5" fill="#ddd"/><path d="M1.5 11c0-3 9-3 9 0z" fill="#ddd"/></svg>LOGIN</span>
        <span><svg viewBox="0 0 12 12"><path d="M6 1v10M1 6h10" stroke="#ddd" stroke-width="1.6"/></svg>SIGNUP</span>
        <span><svg viewBox="0 0 12 12"><rect x="1.5" y="1.5" width="9" height="9" fill="none" stroke="#ddd" stroke-width="1.4"/><path d="M6 3.5v5M3.5 6h5" stroke="#ddd" stroke-width="1.4"/></svg>WALK IN CLINICS</span>
      </nav>
    </div>
  </div>

  <div class="masthead">
    <div class="wrap">
      <div class="brand">YOUR LOGO</div>
      <div class="search">
        <div class="field">Your Search Here</div>
        <div class="scope">Search All Articles <svg width="8" height="6" viewBox="0 0 8 6"><path d="M0 0h8L4 6z" fill="#444"/></svg></div>
        <div class="go"><svg width="14" height="14" viewBox="0 0 14 14"><circle cx="6" cy="6" r="4.3" fill="none" stroke="#fff" stroke-width="1.8"/><path d="M9.2 9.2 13 13" stroke="#fff" stroke-width="2"/></svg></div>
      </div>
      <div class="weather">
        <svg width="14" height="14" viewBox="0 0 14 14"><circle cx="7" cy="7" r="3" fill="#f2a900"/><path d="M7 0v2.5M7 11.5V14M0 7h2.5M11.5 7H14" stroke="#f2a900" stroke-width="1.4"/></svg>
        TUESDAY 01.2016 | 24°C SUNNY
      </div>
    </div>
  </div>

  <nav class="primary-nav">
    <ul class="wrap">
      <li class="active">Home</li><li>News</li><li>Sports</li><li>What's On</li><li>Opinion</li><li>Community</li><li>Obituaries</li><li>Autos</li><li>Classifieds</li><li>Real Estate</li><li>Shopping</li><li>Jobs</li>
    </ul>
  </nav>
</header>

<main class="wrap">
  <div class="ticker">
    <div class="label">Top Stories Here</div>
    <div class="line"><b>»</b>Federal Health Agency approves 1st tablet for gradually reducing hay fever allergy symptoms - @NWS</div>
    <div class="pager" style="margin-right:6px"><i><svg viewBox="0 0 8 8"><path d="M6 0 1 4l5 4z" fill="#fff"/></svg></i><i><svg viewBox="0 0 8 8"><path d="M2 0l5 4-5 4z" fill="#fff"/></svg></i></div>
  </div>

  <!-- top stories + latest -->
  <section class="row r1">
    <div class="hero">
      <div class="shot" role="img" aria-label="Photo of a yellow lifeguard pickup truck parked on a sandy beach under a pale sky"></div>
      <span class="arrow prev"><svg width="10" height="14" viewBox="0 0 10 14"><path d="M8 0 1 7l7 7" fill="none" stroke="#fff" stroke-width="2"/></svg></span>
      <span class="arrow next"><svg width="10" height="14" viewBox="0 0 10 14"><path d="M2 0l7 7-7 7" fill="none" stroke="#fff" stroke-width="2"/></svg></span>
      <div class="caption">
        <h1>Federal Health Agency approves 1st tablet</h1>
        <p>Federal Health Agency approves 1st tablet for gradually reducing hay fever allergy symptoms - @NWS</p>
        <a class="btn-red">Read More</a>
      </div>
    </div>
    <aside>
      <h2 class="side-title">Latest News</h2>
      <ul class="bullets">
        <li>Create a Fun Backyard With Aluminum Fencing</li>
        <li>Smart Kitchen Makeover Ideas to Steal For A Beautiful Home</li>
        <li>Use The Right And Advanced Tree Pruning Equipment</li>
        <li>The Benefits You Get With A Modern Fingerprint Door Lock</li>
        <li>Create a Fun Backyard With Aluminum Fencing</li>
        <li>Smart Kitchen Makeover Ideas to Steal For A Beautiful Home</li>
        <li>Super Water Savings With Innovative Wall Concealed Faucets</li>
      </ul>
      <a class="more-right">Read more »</a>
    </aside>
  </section>

  <!-- breaking + recent -->
  <section class="row r2">
    <div>
      <div class="breaking">
        <div class="label">BREAKING NEWS</div>
        <div class="line">» Federal Health Agency approves symptoms - @NWS</div>
      </div>
      <article class="feature">
        <div class="photo" role="img" aria-label="Photo of a tree-lined city street with tall buildings"></div>
        <div>
          <h3>WNB: New York has, over the last few centuries, become one of the world's most</h3>
          <p>But what if you could redraw the city's map – and build it from scratch? If we were designing New York today, how different would it look? The new New York City would balance the relationship between the information networks that the metropolis depends on and Earth's finite resources. All vital components of life would be monitored and attuned to the needs of every organism.</p>
          <a class="read">Read more »</a>
        </div>
      </article>
    </div>
    <aside>
      <h2 class="side-title">Recent News</h2>
      <ul class="bullets">
        <li>Health News Special</li>
        <li>Top Health News</li>
        <li>Health News Special</li>
        <li>This is a Health News: This is a Health News</li>
        <li>Health News Special: Health News Special</li>
        <li>Affordable Care Act is Working</li>
        <li>US President News</li>
        <li>This is another Political News, Political News</li>
      </ul>
      <a class="more-right">Read more »</a>
    </aside>
  </section>

  <!-- local news -->
  <section class="row r3">
    <div>
      <div class="sec-head"><h2>Latest Local News</h2><div class="pager"><i><svg viewBox="0 0 8 8"><path d="M6 0 1 4l5 4z" fill="#fff"/></svg></i><i><svg viewBox="0 0 8 8"><path d="M2 0l5 4-5 4z" fill="#fff"/></svg></i></div></div>
      <div class="story-grid">
        <article class="story">
          <h3>The Affordable Care Act is Working, 'Helping People Coast To Coast'</h3><span class="meta">Posted On 03 Jan 2015 By John Doe</span>
          <div class="body"><div class="thumb" role="img" aria-label="Photo of a speaker at a podium"></div>President Harlan emerged from the White House on Tuesday to rousing applause. He announced that 7.1 million Americans had signed up for health care through the federal exchanges set up under the new law, passing the original goal set for the first enrollment period.</div>
        </article>
        <article class="story">
          <h3>Tourists from Asia-Pacific to become world's top spenders</h3><span class="meta">Posted On 03 Jan 2015 By John Doe</span>
          <div class="body"><div class="thumb" role="img" aria-label="Photo of tourists in a busy street"></div>SINGAPORE: The Asia-Pacific will overtake Europe as the region whose tourists spend the most money overseas within 10 years, a report said Wednesday, driven by an explosion in the number of travellers leaving the region.</div>
        </article>
        <article class="story">
          <h3>Phoenix, Columbus Eliminated From NPC Convention Contention</h3><span class="meta">Posted On 03 Jan 2015 By John Doe</span>
          <div class="body"><div class="thumb" role="img" aria-label="Photo of a party convention hall"></div>The Unity National Committee trimmed its list of potential 2016 list of convention sites to a half dozen on list of Tuesday, eliminating Phoenix and Columbus. Ohio: the list of contention. That leaves Cincinnati and Cleveland.</div>
        </article>
        <article class="story">
          <h3>The Affordable Care Act is Working, 'Helping People Coast To Coast'</h3><span class="meta">Posted On 03 Jan 2015 By John Doe</span>
          <div class="body"><div class="thumb" role="img" aria-label="Photo of a speaker at a podium"></div>President Harlan emerged from the White House on Tuesday to rousing applause. He announced that 7.1 million Americans had signed up for health care through the federal exchanges set up under the new law.</div>
        </article>
      </div>
    </div>
    <aside>
      <h2 class="side-title">Neighbour News</h2>
      <div class="tabs"><span class="on">Today</span><span>Latest</span><span>Popular</span></div>
      <ul class="bullets">
        <li>Create a Fun Backyard With Aluminum Fencing</li>
        <li>Smart Kitchen Makeover Ideas to Steal For A Beautiful Home</li>
        <li>Use The Right And Advanced Tree Pruning Equipment</li>
        <li>The Benefits You Get With A Modern Fingerprint Door Lock</li>
        <li>Create a Fun Backyard With Aluminum Fencing</li>
        <li>Smart Kitchen Makeover Ideas to Steal For A Beautiful Home</li>
      </ul>
      <a class="more-right">Read more »</a>
    </aside>
  </section>

  <!-- videos -->
  <section class="row r4">
    <div>
      <div class="sec-head"><h2>Top Videos Here</h2><div class="pager"><i><svg viewBox="0 0 8 8"><path d="M6 0 1 4l5 4z" fill="#fff"/></svg></i><i><svg viewBox="0 0 8 8"><path d="M2 0l5 4-5 4z" fill="#fff"/></svg></i></div></div>
      <div class="video-grid">
        <article class="video"><div class="frame" role="img" aria-label="Video still of a politician speaking"><svg viewBox="0 0 48 48"><circle cx="24" cy="24" r="22" fill="rgba(0,0,0,.5)" stroke="#fff" stroke-width="2"/><path d="M19 14l14 10-14 10z" fill="#fff"/></svg></div><h3>Phoenix, Columbus Columbus Elioi Contention</h3></article>
        <article class="video"><div class="frame" role="img" aria-label="Video still of a speaker at a podium"><svg viewBox="0 0 48 48"><circle cx="24" cy="24" r="22" fill="rgba(0,0,0,.5)" stroke="#fff" stroke-width="2"/><path d="M19 14l14 10-14 10z" fill="#fff"/></svg></div><h3>Phoenix, Columbus Columbus Elioi Contention</h3></article>
        <article class="video"><div class="frame" role="img" aria-label="Video still of a speaker in front of a technology banner"><svg viewBox="0 0 48 48"><circle cx="24" cy="24" r="22" fill="rgba(0,0,0,.5)" stroke="#fff" stroke-width="2"/><path d="M19 14l14 10-14 10z" fill="#fff"/></svg></div><h3>Phoenix, Columbus Columbus Elioi Contention</h3></article>
      </div>
    </div>
    <aside>
      <h2 class="side-title">Other Videos</h2>
      <ul class="vlist">
        <li><div class="vthumb" role="img" aria-label="Video still of a politician"><svg viewBox="0 0 24 24"><circle cx="12" cy="12" r="11" fill="rgba(0,0,0,.5)"/><path d="M9.5 7l7 5-7 5z" fill="#fff"/></svg></div><div><b>Phoenix, Columbus</b><p>Federal Health Agency approves 1st tablet for</p></div></li>
        <li><div class="vthumb" role="img" aria-label="Video still of a press conference"><svg viewBox="0 0 24 24"><circle cx="12" cy="12" r="11" fill="rgba(0,0,0,.5)"/><path d="M9.5 7l7 5-7 5z" fill="#fff"/></svg></div><div><b>Eliminated From NPC</b><p>Federal Health Agency approves 1st tablet for</p></div></li>
        <li><div class="vthumb" role="img" aria-label="Video still of a city street"><svg viewBox="0 0 24 24"><circle cx="12" cy="12" r="11" fill="rgba(0,0,0,.5)"/><path d="M9.5 7l7 5-7 5z" fill="#fff"/></svg></div><div><b>Columbus Eliminated</b><p>Federal Health Agency proves 1st tablet for</p></div></li>
      </ul>
    </aside>
  </section>

  <!-- sports -->
  <section class="row r5">
    <div>
      <div class="sec-head"><h2>Sports News</h2><div class="pager"><i><svg viewBox="0 0 8 8"><path d="M6 0 1 4l5 4z" fill="#fff"/></svg></i><i><svg viewBox="0 0 8 8"><path d="M2 0l5 4-5 4z" fill="#fff"/></svg></i></div></div>
      <div class="card-grid">
        <article class="card"><div class="pic" role="img" aria-label="Sports photo"></div><h3>Phoenix, Columbus Elioi Contention</h3><p class="meta">03 Jan 2015</p><p>Tuesday, eliminating Phoenix contention. That leaves Cincin Tuesday, eliminating Phoenix contention.</p><a class="read">Read more »</a></article>
        <article class="card"><div class="pic" role="img" aria-label="Sports photo"></div><h3>Phoenix, Columbus Elioi Contention</h3><p class="meta">03 Jan 2015</p><p>Tuesday, eliminating Phoenix contention. That leaves Cincin Tuesday, eliminating Phoenix contention.</p><a class="read">Read more »</a></article>
        <article class="card"><div class="pic" role="img" aria-label="Sports photo"></div><h3>Phoenix, Columbus Elioi Contention</h3><p class="meta">03 Jan 2015</p><p>Tuesday, eliminating Phoenix contention. That leaves Cincin Tuesday, eliminating Phoenix contention.</p><a class="read">Read more »</a></article>
        <article class="card"><div class="pic" role="img" aria-label="Sports photo"></div><h3>Phoenix, Columbus Elioi Contention</h3><p class="meta">03 Jan 2015</p><p>Tuesday, eliminating Phoenix contention. That leaves Cincin Tuesday, eliminating Phoenix contention.</p><a class="read">Read more »</a></article>
      </div>
    </div>
    <aside>
      <h2 class="side-title">More Sports News</h2>
      <ul class="bullets">
        <li>Health News Special</li><li>Top Health News</li><li>Health News Special</li><li>Affordable Care Act is Working</li><li>US President News</li><li>This is another Political News</li><li>Health News Special</li><li>Top Health News</li>
      </ul>
      <a class="more-right">Read more »</a>
    </aside>
  </section>

  <!-- US -->
  <section class="row r6">
    <div>
      <div class="sec-head"><h2>US News</h2><div class="pager"><i><svg viewBox="0 0 8 8"><path d="M6 0 1 4l5 4z" fill="#fff"/></svg></i><i><svg viewBox="0 0 8 8"><path d="M2 0l5 4-5 4z" fill="#fff"/></svg></i></div></div>
      <div class="story-grid">
        <article class="story">
          <h3>The Affordable Care Act is Working, 'Helping People Coast To Coast'</h3><span class="meta">Posted On 03 Jan 2015 By John Doe</span>
          <div class="body"><div class="thumb" role="img" aria-label="Photo of a speaker at a podium"></div>President Harlan emerged from the White House on Tuesday to rousing applause. He announced that 7.1 million Americans had signed up for health care through the federal exchanges set up under the new law.</div>
        </article>
        <article class="story">
          <h3>Tourists from Asia-Pacific to become world's top spenders</h3><span class="meta">Posted On 03 Jan 2015 By John Doe</span>
          <div class="body"><div class="thumb" role="img" aria-label="Photo of tourists in a busy street"></div>SINGAPORE: The Asia-Pacific will overtake Europe as the region whose tourists spend the most money overseas within 10 years, a report said Wednesday, driven by an explosion in the number of travellers.</div>
        </article>
      </div>
    </div>
    <aside>
      <h2 class="side-title">More US News</h2>
      <ul class="bullets">
        <li>Health News Special</li><li>Top Health News</li><li>Health News Special</li><li>Top Health News</li><li>Health News Special</li><li>Affordable Care Act is Working</li><li>US President News</li>
      </ul>
      <a class="more-right">Read more »</a>
    </aside>
  </section>

  <!-- world -->
  <section class="row r7">
    <div>
      <div class="sec-head"><h2>World News</h2><div class="pager"><i><svg viewBox="0 0 8 8"><path d="M6 0 1 4l5 4z" fill="#fff"/></svg></i><i><svg viewBox="0 0 8 8"><path d="M2 0l5 4-5 4z" fill="#fff"/></svg></i></div></div>
      <div class="tabs inline"><span class="on">Asia</span><span>Europe</span><span>Others</span></div>
      <div class="card-grid">
        <article class="card"><div class="pic" role="img" aria-label="World news photo"></div><h3>Phoenix, Columbus Elioi Contention</h3><p class="meta">03 Jan 2015</p><p>Tuesday, eliminating Phoenix contention. That leaves Cincin Tuesday, eliminating Phoenix contention.</p><a class="read">Read more »</a></article>
        <article class="card"><div class="pic" role="img" aria-label="World news photo"></div><h3>Phoenix, Columbus Elioi Contention</h3><p class="meta">03 Jan 2015</p><p>Tuesday, eliminating Phoenix contention. That leaves Cincin Tuesday, eliminating Phoenix contention.</p><a class="read">Read more »</a></article>
        <article class="card"><div class="pic" role="img" aria-label="World news photo"></div><h3>Phoenix, Columbus Elioi Contention</h3><p class="meta">03 Jan 2015</p><p>Tuesday, eliminating Phoenix contention. That leaves Cincin Tuesday, eliminating Phoenix contention.</p><a class="read">Read more »</a></article>
        <article class="card"><div class="pic" role="img" aria-label="World news photo"></div><h3>Phoenix, Columbus Elioi Contention</h3><p class="meta">03 Jan 2015</p><p>Tuesday, eliminating Phoenix contention. That leaves Cincin Tuesday, eliminating Phoenix contention.</p><a class="read">Read more »</a></article>
      </div>
    </div>
    <aside>
      <h2 class="side-title">Others News</h2>
      <ul class="bullets">
        <li>This is a Health News: This is a Health News</li><li>Health News Special</li><li>Health News Special: Health News Special</li><li>US President News</li><li>This is another Political News, Political News</li><li>This is a Health News: This is a Health News</li><li>Health News Special: Health News Special</li><li>Affordable Care Act is Working</li>
      </ul>
      <a class="more-right">Read more »</a>
    </aside>
  </section>

  <!-- politics -->
  <section class="row r8">
    <div>
      <div class="sec-head"><h2>Political News</h2><div class="pager"><i><svg viewBox="0 0 8 8"><path d="M6 0 1 4l5 4z" fill="#fff"/></svg></i><i><svg viewBox="0 0 8 8"><path d="M2 0l5 4-5 4z" fill="#fff"/></svg></i></div></div>
      <div class="card-grid">
        <article class="card"><div class="pic" role="img" aria-label="Political news photo"></div><h3>Phoenix, Columbus Elioi Contention</h3><p class="meta">03 Jan 2015</p><p>Tuesday, eliminating Phoenix contention. That leaves Cincin Tuesday, eliminating Phoenix contention.</p><a class="read">Read more »</a></article>
        <article class="card"><div class="pic" role="img" aria-label="Political news photo"></div><h3>Phoenix, Columbus Elioi Contention</h3><p class="meta">03 Jan 2015</p><p>Tuesday, eliminating Phoenix contention. That leaves Cincin Tuesday, eliminating Phoenix contention.</p><a class="read">Read more »</a></article>
        <article class="card"><div class="pic" role="img" aria-label="Political news photo"></div><h3>Phoenix, Columbus Elioi Contention</h3><p class="meta">03 Jan 2015</p><p>Tuesday, eliminating Phoenix contention. That leaves Cincin Tuesday, eliminating Phoenix contention.</p><a class="read">Read more »</a></article>
        <article class="card"><div class="pic" role="img" aria-label="Political news photo"></div><h3>Phoenix, Columbus Elioi Contention</h3><p class="meta">03 Jan 2015</p><p>Tuesday, eliminating Phoenix contention. That leaves Cincin Tuesday, eliminating Phoenix contention.</p><a class="read">Read more »</a></article>
      </div>
    </div>
    <aside>
      <h2 class="side-title">Political News</h2>
      <ul class="bullets">
        <li>Health News Special</li><li>Top Health News</li><li>Health News Special</li><li>Top Health News</li><li>Health News Special</li><li>Affordable Care Act is Working</li><li>US President News</li>
      </ul>
      <a class="more-right">Read more »</a>
    </aside>
  </section>

  <!-- science -->
  <section class="row r9">
    <div>
      <div class="sec-head"><h2>Science News</h2><div class="pager"><i><svg viewBox="0 0 8 8"><path d="M6 0 1 4l5 4z" fill="#fff"/></svg></i><i><svg viewBox="0 0 8 8"><path d="M2 0l5 4-5 4z" fill="#fff"/></svg></i></div></div>
      <div class="story-grid">
        <article class="story">
          <h3>The Affordable Care Act is Working, 'Helping People Coast To Coast'</h3><span class="meta">Posted On 03 Jan 2015 By John Doe</span>
          <div class="body"><div class="thumb" role="img" aria-label="Photo of a speaker at a podium"></div>President Harlan emerged from the White House on Tuesday to rousing applause. He announced that 7.1 million Americans had signed up for health care through the federal exchanges set up under the new law.</div>
        </article>
        <article class="story">
          <h3>Tourists from Asia-Pacific to become world's top spenders</h3><span class="meta">Posted On 03 Jan 2015 By John Doe</span>
          <div class="body"><div class="thumb" role="img" aria-label="Photo of tourists in a busy street"></div>SINGAPORE: The Asia-Pacific will overtake Europe as the region whose tourists spend the most money overseas within 10 years, a report said Wednesday, driven by an explosion in the number of travellers.</div>
        </article>
      </div>
    </div>
    <aside>
      <h2 class="side-title">More Science News</h2>
      <ul class="bullets">
        <li>Health News Special</li><li>Top Health News</li><li>Health News Special</li><li>Top Health News</li><li>Health News Special</li><li>Affordable Care Act is Working</li><li>US President News</li>
      </ul>
      <a class="more-right">Read more »</a>
    </aside>
  </section>

  <!-- around the web -->
  <section class="row r10">
    <div>
      <div class="sec-head"><h2>News Around The Web</h2><div class="pager"><i><svg viewBox="0 0 8 8"><path d="M6 0 1 4l5 4z" fill="#fff"/></svg></i><i><svg viewBox="0 0 8 8"><path d="M2 0l5 4-5 4z" fill="#fff"/></svg></i></div></div>
      <div class="card-grid">
        <article class="card"><div class="pic" role="img" aria-label="Photo of a crowd at an outdoor event"></div><h3>Phoenix, Columbus Elioi Contention</h3><p class="meta">03 Jan 2015</p><p>Tuesday, eliminating Phoenix contention. That leaves Cincin Tuesday, eliminating Phoenix contention.</p><a class="read">Read more »</a></article>
        <article class="card"><div class="pic" role="img" aria-label="Photo of a crowd at an outdoor event"></div><h3>Phoenix, Columbus Elioi Contention</h3><p class="meta">03 Jan 2015</p><p>Tuesday, eliminating Phoenix contention. That leaves Cincin Tuesday, eliminating Phoenix contention.</p><a class="read">Read more »</a></article>
        <article class="card"><div class="pic" role="img" aria-label="Photo of a crowd at an outdoor event"></div><h3>Phoenix, Columbus Elioi Contention</h3><p class="meta">03 Jan 2015</p><p>Tuesday, eliminating Phoenix contention. That leaves Cincin Tuesday, eliminating Phoenix contention.</p><a class="read">Read more »</a></article>
        <article class="card"><div class="pic" role="img" aria-label="Photo of a speaker at a podium"></div><h3>Phoenix, Columbus Elioi Contention</h3><p class="meta">03 Jan 2015</p><p>Tuesday, eliminating Phoenix contention. That leaves Cincin Tuesday, eliminating Phoenix contention.</p><a class="read">Read more »</a></article>
      </div>
    </div>
    <aside>
      <h2 class="side-title">More News</h2>
      <ul class="bullets">
        <li>Health News Special</li><li>Top Health News</li><li>This is a Health News: This is a Health News</li><li>Health News Special: Health News Special</li><li>Affordable Care Act is Working</li><li>US President News</li>
      </ul>
      <a class="more-right">Read more »</a>
    </aside>
  </section>

  <!-- entertainment -->
  <section class="row r11">
    <div>
      <div class="sec-head"><h2>Music &amp; Entertainment</h2><div class="pager"><i><svg viewBox="0 0 8 8"><path d="M6 0 1 4l5 4z" fill="#fff"/></svg></i><i><svg viewBox="0 0 8 8"><path d="M2 0l5 4-5 4z" fill="#fff"/></svg></i></div></div>
      <div class="card-grid">
        <article class="card"><div class="pic" role="img" aria-label="Entertainment photo"></div><h3>Phoenix, Columbus Elioi Contention</h3><p class="meta">03 Jan 2015</p><p>Tuesday, eliminating Phoenix contention. That leaves Cincin Tuesday, eliminating Phoenix contention.</p><a class="read">Read more »</a></article>
        <article class="card"><div class="pic" role="img" aria-label="Entertainment photo"></div><h3>Phoenix, Columbus Elioi Contention</h3><p class="meta">03 Jan 2015</p><p>Tuesday, eliminating Phoenix contention. That leaves Cincin Tuesday, eliminating Phoenix contention.</p><a class="read">Read more »</a></article>
        <article class="card"><div class="pic" role="img" aria-label="Entertainment photo"></div><h3>Phoenix, Columbus Elioi Contention</h3><p class="meta">03 Jan 2015</p><p>Tuesday, eliminating Phoenix contention. That leaves Cincin Tuesday, eliminating Phoenix contention.</p><a class="read">Read more »</a></article>
        <article class="card"><div class="pic" role="img" aria-label="Entertainment photo"></div><h3>Phoenix, Columbus Elioi Contention</h3><p class="meta">03 Jan 2015</p><p>Tuesday, eliminating Phoenix contention. That leaves Cincin Tuesday, eliminating Phoenix contention.</p><a class="read">Read more »</a></article>
      </div>
    </div>
    <aside>
      <h2 class="side-title">Entertainment News</h2>
      <ul class="bullets">
        <li>Health News Special</li><li>Top Health News</li><li>Health News Special</li><li>This is a Health News: This is a Health News</li><li>Health News Special: Health News Special</li><li>Affordable Care Act is Working</li><li>US President News</li><li>This is another Political News, Political News</li>
      </ul>
      <a class="more-right">Read more »</a>
    </aside>
  </section>
</main>

<footer>
  <div class="site-footer">
    <div class="wrap">
      <div><h4>Hills Info</h4><ul><li>About us</li><li>Accessible customer service policy</li><li>Commenting guidelines</li><li>Commitment to accessibility</li><li>Sitemap</li><li>Staff directory</li><li>Work for us</li></ul></div>
      <div><h4>Local Info</h4><ul><li>Announcements</li><li>Cars</li><li>Classifieds</li><li>Deals</li><li>Travel</li><li>Autolisting.com</li></ul></div>
      <div><h4>Community Sites</h4><ul><li>Brookfieldherald.com</li><li>Ridgevalepost.com</li><li>Millbrookgazette.com</li><li>Insidehollow.com</li><li>Westerndales.ca</li><li>Thebeacon.com</li></ul></div>
      <div><h4>Resources</h4><ul><li>Pagefinder.ca</li><li>Rinkreport.ca</li><li>Coveragedesk.com</li><li>Leaderboard.ca</li></ul></div>
      <div><h4>Affiliates &amp; Partners</h4><ul><li>Lakeside Star</li><li>Lakeside.com</li><li>Transit Daily</li><li>JobHarbor</li></ul></div>
    </div>
  </div>
  <div class="legal">
    <div class="wrap">
      <nav><span>Hillside News</span><span>Advertising Terms</span><span>Terms of Use</span><span>Corporate Privacy Policy</span></nav>
      <span>© Copyright 2016 Daily World Report</span>
    </div>
  </div>
</footer>

</body>
</html>
```